Marketing Brochure - Conjunction event

We need a brochure for clients/conjunction real estate agents to view the type of projects VARO531 have available.
As a guideline of our requirements, please refer to our company profile. As you can see it is a simple elegant professional image we are after.
We are a Real Estate company specialise in off the plans project marketing. We have sale teams to sell the projects/ residential properties but also conjunction with other real estate agents. This is the first time we decided to use QuillMarket to design our brochure. If pleasing results, ongoing we will have many more design projects to do.

Target Market(s)

Clients / real estate agents

Industry/Entity Type

Real Estate

Font styles to use
Sans Serif

Colors
ffffff
ef484e

Requirements
Must have
• All the details in the documents, Encourage creative designs.
• Company logo and the black banner as seen on company profile brochure
Nice to have
• similar to our company profile brochure( file attached)
Should not have
• Funky or too loud type image

```html
<!DOCTYPE html>
<html lang="en">
<head>
<meta charset="utf-8">
<title>VARO531 – Conjunction Agent Event Brochure</title>
<link href="https://fonts.googleapis.com/css2?family=Oswald:wght@500;700&family=Lato:wght@400;700;900&display=swap" rel="stylesheet">
<style>
:root{
  --orange:#ef4a23;
  --red:#ef484e;
  --dark:#2b2829;
  --darker:#1e1c1d;
  --white:#ffffff;
  --paper:#f4f4f4;
  --grey:#8a8a8a;
  --bg:#d9d9d9;
  --text:#333;
}
*{margin:0;padding:0;box-sizing:border-box}
html,body{width:1200px;height:1200px;overflow:hidden;background:var(--bg);font-family:"Lato",sans-serif;color:var(--text)}
.spread{position:absolute;left:20px;width:1160px;height:560px;display:flex;box-shadow:0 4px 14px rgba(0,0,0,.25)}
.spread--outer{top:20px}
.spread--inner{top:620px}
.page{position:relative;width:580px;height:560px;background:var(--white);overflow:hidden}
.page + .page{border-left:1px solid #ddd}

/* disclaimer page */
.disclaimer__band{position:absolute;left:0;top:0;width:580px;height:150px}
.disclaimer__title{position:absolute;left:40px;top:60px;font-family:"Oswald",sans-serif;font-weight:700;font-size:30px;color:var(--white);letter-spacing:1px}
.disclaimer__body{position:absolute;left:40px;top:175px;width:500px;font-size:9.5px;line-height:1.5;color:#444}
.disclaimer__body p{margin-bottom:9px}

/* cover page */
.cover__photo{position:absolute;left:0;top:0;width:580px;height:560px;background:linear-gradient(160deg,#e8e8e8 0%,#9a9a9a 45%,#4a4a4a 80%,#2a2a2a 100%)}
.cover__topband{position:absolute;left:0;top:0;width:580px;height:110px;background:var(--dark)}
.cover__stripe{position:absolute;left:0;top:110px;width:580px;height:40px}
.brand{font-family:"Lato",sans-serif;font-weight:900;color:var(--orange);display:flex;align-items:center;gap:8px}
.brand__dot{width:14px;height:14px;background:var(--orange)}
.cover__brand{position:absolute;left:30px;top:38px;font-size:34px}
.cover__circle{position:absolute;right:40px;top:20px;width:140px;height:140px;border-radius:50%;border:4px solid var(--white);background:radial-gradient(circle at 40% 40%,#f0f0f0,#7a7a7a)}
.cover__title{position:absolute;left:30px;bottom:60px;font-family:"Oswald",sans-serif;font-weight:700;line-height:1}
.cover__title .t1{display:block;font-size:56px;color:var(--orange)}
.cover__title .t2{display:block;font-size:48px;color:var(--white);background:var(--dark);padding:2px 10px;margin-top:4px}

/* inner spread */
.inner__top{position:absolute;left:0;top:0;width:580px;height:40px;background:var(--dark)}
.inner__tab{position:absolute;top:0;height:58px;background:var(--orange);font-family:"Oswald",sans-serif;font-weight:700;color:var(--white);font-size:24px;display:flex;align-items:center;padding-left:30px}
.inner__tab span{color:var(--dark);margin:0 8px}
.badge{position:absolute;left:18px;top:48px;width:100px;height:100px;border-radius:50%;border:5px solid var(--orange);background:var(--white);display:flex;align-items:center;justify-content:center;font-size:17px}
.address{position:absolute;font-weight:900;font-size:12px;line-height:1.25;color:var(--dark)}
.project{position:absolute;font-family:"Oswald",sans-serif;font-weight:700;line-height:1.05;color:var(--dark)}
.project .name{font-size:20px}
.project .suburb{font-size:15px;color:var(--orange);font-family:"Lato",sans-serif;font-weight:700}
.project .status{font-size:26px;color:var(--orange)}
.project .note{font-size:12px;font-family:"Lato",sans-serif;font-weight:700}
.photo{position:absolute;height:72px;border:4px solid var(--dark);border-radius:8px;background:linear-gradient(180deg,#7fb3e0 0%,#c9dcee 45%,#b89a76 75%,#6d6156 100%)}
.label{position:absolute;height:16px;background:var(--dark);color:var(--orange);font-size:10.5px;font-weight:900;padding:1px 8px}
.label--orange{background:var(--orange);color:var(--dark)}
.value{position:absolute;font-size:10.5px;font-weight:900;color:var(--orange)}
.list{position:absolute;font-size:8.5px;line-height:1.35;color:#333;list-style:none}
.list li::before{content:"• "}
.table{position:absolute;border-collapse:collapse;font-size:9px;text-align:center}
.table th{background:var(--orange);color:var(--dark);font-weight:900;padding:4px 3px;line-height:1.15}
.table td{background:var(--dark);color:var(--white);padding:5px 3px;border-top:1px solid #555}
.table tr:nth-child(even) td{background:#3a3637}
.bgfade{position:absolute;left:0;bottom:0;width:580px;height:130px;background:linear-gradient(180deg,rgba(255,255,255,0),#cfcfcf)}
</style>
</head>
<body>

<!-- Outer spread: disclaimer back page + front cover -->
<section class="spread spread--outer">
  <article class="page page--disclaimer">
    <svg class="disclaimer__band" viewBox="0 0 580 150" aria-hidden="true">
      <polygon points="0,0 580,0 580,20 0,130" fill="#2b2829"/>
      <polygon points="0,45 580,0 580,110 0,150" fill="#ef4a23"/>
    </svg>
    <h2 class="disclaimer__title">DISCLAMER</h2>
    <div class="disclaimer__body">
      <p>This document has been prepared by VARO531 for the purpose of providing information to potential purchasers. It is provided on a confidential basis and is not to be distributed or reproduced in whole or in part without the prior written consent of VARO531.</p>
      <p>This document does not purport to contain all the information that a potential purchaser or other interested party may require. It does not take into account the objectives or financial situation of any person and is intended as a guide only. It does not constitute advice, an offer or a contract.</p>
      <p>Any potential purchaser should obtain independent financial, taxation, accounting and legal advice before making any decision with respect to a property.</p>
      <p>This document may contain information prepared by third parties. Figures and calculations have not been independently verified by VARO531 and are estimates only.</p>
      <p>Past performance of any property is not a reliable indication of future performance. All prices are GST inclusive unless stated otherwise.</p>
      <p>Users should not rely on any information in this document as a statement of fact and must make their own enquiries. No warranty is given as to accuracy, and no liability is accepted for any loss arising from its use.</p>
    </div>
  </article>

  <article class="page page--cover">
    <div class="cover__photo" role="img" aria-label="Black and white photo of a modern multi-storey apartment building with balconies"></div>
    <div class="cover__topband"></div>
    <svg class="cover__stripe" viewBox="0 0 580 40" aria-hidden="true">
      <polygon points="0,0 580,0 580,14 0,40" fill="#ef4a23"/>
    </svg>
    <div class="brand cover__brand"><span class="brand__dot"></span>VARO531</div>
    <div class="cover__circle" role="img" aria-label="Circular inset photo of apartment rooftop and courtyard"></div>
    <h1 class="cover__title"><span class="t1">CONJUNCTION</span><span class="t2">AGENT EVENT</span></h1>
  </article>
</section>

<!-- Inner spread: projects to sell -->
<section class="spread spread--inner">
  <article class="page page--project">
    <div class="bgfade"></div>
    <div class="inner__top"></div>
    <div class="badge"><div class="brand"><span>VARO531</span></div></div>
    <div class="address" style="left:135px;top:58px">210-236 Harbour<br>Road Lakemont<br>NSW 2205</div>
    <div class="project" style="left:300px;top:52px;text-align:center">
      <div class="name">The Meridian</div>
      <div class="suburb">Lakemont Sydney is</div>
      <div class="status">SOLD OUT</div>
    </div>
    <div class="photo" style="left:24px;top:150px;width:170px" role="img" aria-label="Photo of a mid-rise apartment complex"></div>
    <div class="photo" style="left:215px;top:150px;width:170px" role="img" aria-label="Rendering of the apartment building at dusk"></div>

    <div class="label" style="left:18px;top:242px;width:230px">Developer</div>
    <div class="value" style="left:26px;top:261px">Brightvale Corp</div>
    <div class="label" style="left:18px;top:280px;width:230px">Architect</div>
    <div class="value" style="left:26px;top:299px">Harlow Pike</div>
    <div class="label" style="left:18px;top:318px;width:230px">Builder</div>
    <div class="value" style="left:26px;top:337px">Brightvale Construction</div>
    <div class="label label--orange" style="left:18px;top:356px;width:230px">Estimated Completion</div>
    <div class="value" style="left:26px;top:376px">End of 2017</div>
    <div class="label label--orange" style="left:18px;top:396px;width:230px">Building Atributes</div>
    <ul class="list" style="left:26px;top:416px">
      <li>Apartments over 6 levels</li>
      <li>Ground Floor retail and restaurant</li>
    </ul>

    <div class="label" style="left:258px;top:236px;width:300px">Feature Include</div>
    <ul class="list" style="left:266px;top:256px;width:290px">
      <li>Mix of spacious 1 &amp; 2 bedroom apartments</li>
      <li>Just 10 km South of Sydney CBD</li>
      <li>Only 3 min to Lakemont train station</li>
      <li>6 min drive to Sydney airport</li>
      <li>5 min walk to the local public school</li>
      <li>Close to Lakemont village and major shopping centre</li>
      <li>Stroll along the promenade beside the water in Sandhaven</li>
      <li>Close to the proposed business technology park – Reed Cove</li>
      <li>Easy access to M5</li>
    </ul>
    <div class="label" style="left:258px;top:392px;width:300px">Deposit Requirement</div>
    <ul class="list" style="left:266px;top:412px"><li>10% deposit (Cash Deposit, Bank Guarantee)</li></ul>

    <table class="table" style="left:18px;top:440px;width:420px">
      <tr><th>Apt<br>Type</th><th>No.<br>Available</th><th>Internal<br>Size (sqm)</th><th>Price Range</th><th>Rental estimate<br>Per week</th><th>Anual<br>Strata Levies</th></tr>
      <tr><td>Studio</td><td>1</td><td>50-55</td><td>-</td><td>$440</td><td>$500-$600</td></tr>
      <tr><td>1 Bed</td><td>35</td><td>72-105</td><td>$564k-$567k</td><td>$480-$550</td><td>$600-$800</td></tr>
      <tr><td>2 Bed</td><td>148</td><td>45</td><td>$687k-$700k</td><td>$580-$700</td><td>$700-$900</td></tr>
      <tr><td>3 Bed</td><td>3</td><td>110</td><td>$687k</td><td>$750-$800</td><td>$1000+</td></tr>
    </table>
  </article>

  <article class="page page--project">
    <div class="bgfade"></div>
    <div class="inner__top"></div>
    <div class="inner__tab" style="left:0;width:580px">PROJECTS <span>TO</span> SELL SYDNEY</div>
    <div class="project" style="left:20px;top:78px">
      <div class="name">The Ridge Quarter</div>
      <div class="suburb">Fernhill Sydney</div>
      <div class="note">Stage II – Launch Next Week</div>
    </div>
    <div class="address" style="left:310px;top:72px">41-57 Elmstone Drive,<br>Fernhill NSW 2155</div>
    <div class="photo" style="left:24px;top:138px;width:175px" role="img" aria-label="Rendering of a modern apartment block with yellow accents"></div>
    <div class="photo" style="left:310px;top:110px;width:175px" role="img" aria-label="Rendering of the apartment development from the street"></div>

    <div class="label" style="left:18px;top:232px;width:220px">Developer</div>
    <div class="value" style="left:26px;top:251px">Brightvale Corp</div>
    <div class="label" style="left:18px;top:270px;width:220px">Architect</div>
    <div class="value" style="left:26px;top:289px">Harlow Pike</div>
    <div class="label" style="left:18px;top:308px;width:220px">Builder</div>
    <div class="value" style="left:26px;top:327px">Brightvale Construction</div>
    <div class="label label--orange" style="left:18px;top:346px;width:220px">Estimated Completion</div>
    <div class="value" style="left:26px;top:366px">Mid 2017</div>
    <div class="label label--orange" style="left:18px;top:386px;width:220px">Building Atributes</div>
    <ul class="list" style="left:26px;top:406px">
      <li>208 Apartments over 6 levels</li>
      <li>14 Ground Floor retail and restaurant</li>
    </ul>

    <div class="label" style="left:250px;top:200px;width:310px">Feature Include</div>
    <ul class="list" style="left:258px;top:220px;width:300px">
      <li>Mix of spacious 1 &amp; 2 bedroom apartments</li>
      <li>Just 42 km Northwest of Sydney CBD</li>
      <li>Close to Fernhill Plaza shopping centre</li>
      <li>Close to local public and high schools</li>
      <li>Close to Westgate Business Park</li>
      <li>Close to the private hospital</li>
      <li>Easily accessible by the M2 Motorway</li>
      <li>Minutes to Fernhill new train station</li>
      <li>Close to the local sporting complex</li>
    </ul>
    <div class="label" style="left:250px;top:350px;width:310px">Deposit Requirement</div>
    <ul class="list" style="left:258px;top:370px"><li>10% deposit (Cash Deposit, Bank Guarantee)</li></ul>

    <table class="table" style="left:18px;top:440px;width:545px">
      <tr><th>Apt<br>Type</th><th>No.<br>Available</th><th>Internal<br>Size (sqm)</th><th>Price Range</th><th>Rental estimate<br>Per week</th><th>Anual<br>Strata Levies</th></tr>
      <tr><td>1 Bed</td><td>13</td><td>Approx 70</td><td>From high 400K</td><td>$440-$490</td><td>$550-$740 per qtr</td></tr>
      <tr><td>2 Bed</td><td>162</td><td>Approx 90</td><td>High 500K</td><td>$520-$570</td><td>$750-$1000</td></tr>
      <tr><td>3 Bed</td><td>34</td><td>Approx 110</td><td>Low 700K</td><td>$650-$710</td><td>$900-$1200</td></tr>
    </table>
  </article>
</section>

</body>
</html>
```